Custom Home Builder Website

We need a re-design of a website for our client: "http://www.dorvelbuildworks.com". Their current design is outdated and has flash. We need to make it responsive for all devices and with a more professional look.

Pages to consider:
1. Home page
2. Portfolio page - gallery of projects (multiple images of a project with captions, and a main text area for each project).

Good clean design reflecting quality craftsmanship is a must.

We only need designs, no coding required

Target Market(s)

The intended market is home owners looking to build with a reputable and professional home builder.

Industry/Entity Type

Home Builder

Requirements
Must have
• Must Have:
• - main areas of site: home, portfolio, video gallery, contact
Nice to have
• - Maybe pullquotes from testimonials placed as slideshow?

```html
<!DOCTYPE html>
<html lang="en">
<head>
<meta charset="utf-8">
<title>Dorvel Buildworks – Custom Home Builder</title>
<link rel="stylesheet" href="https://fonts.googleapis.com/css2?family=Roboto:wght@400;500&family=PT+Sans:wght@400;700&display=swap">
<style>
  :root {
    --header-bg: #ebebeb;
    --brown: #5a3d0d;
    --white: #ffffff;
    --ink: #1e1e1e;
    --muted: #6a6a6a;
    --accent-red: #c8201f;
    --arrow-red: #8a1620;
    --tan: #b8996a;
    --news-bg: #eef0e6;
    --footer-bg: #d5d7cb;
    --rule: #c9c9c9;
    --button-dark: #2e2a25;
    --field-bg: #f3f3ee;
    --submit-bg: #5c5c5c;
  }
  * { box-sizing: border-box; margin: 0; padding: 0; }
  html, body { width: 1200px; height: 776px; overflow: hidden; }
  body {
    position: relative;
    background: var(--header-bg);
    font-family: "PT Sans", Verdana, sans-serif;
    color: var(--ink);
  }
  .site-header { position: absolute; inset: 0 0 auto 0; height: 127px; background: var(--header-bg); }
  .brand {
    position: absolute; left: 52px; top: 52px;
    font-family: "Roboto", sans-serif; font-weight: 500; font-size: 27px;
    letter-spacing: 2px; color: var(--tan); text-transform: uppercase;
  }
  .utility-nav {
    position: absolute; left: 714px; width: 412px; top: 16px;
    display: flex; justify-content: space-between;
    padding: 0 0 9px 33px; border-bottom: 1px solid var(--rule);
  }
  .utility-nav a, .main-nav a {
    font-family: "Roboto", sans-serif; text-decoration: none; text-transform: uppercase;
  }
  .utility-nav a { font-size: 11.5px; color: var(--muted); }
  .main-nav {
    position: absolute; left: 550px; width: 576px; top: 53px;
    display: flex; justify-content: space-between;
  }
  .main-nav a { font-size: 13px; color: var(--ink); }
  .main-nav a.is-current { color: var(--accent-red); text-transform: none; }

  .hero { position: absolute; left: 0; top: 127px; width: 1200px; height: 553px; background: var(--brown); }
  .hero-copy { position: absolute; left: 51px; top: 50px; width: 385px; color: var(--white); }
  .hero-copy h1 { font-size: 19px; font-weight: 700; margin-bottom: 20px; }
  .hero-copy p { font-size: 12.6px; line-height: 14.8px; margin-bottom: 14.8px; }
  .read-more {
    position: absolute; left: 315px; top: 296px; width: 84px; height: 26px;
    background: var(--button-dark); color: var(--white); font-size: 12px;
    display: flex; align-items: center; justify-content: center; text-decoration: none;
  }
  .hero-photo {
    position: absolute; left: 490px; top: 93px; width: 648px; height: 568px; border-radius: 14px;
    background: linear-gradient(135deg, #c9c3b8 0%, #8f877a 35%, #b77a3c 65%, #d99a52 100%);
  }
  .slide-next { position: absolute; left: 1141px; top: 350px; width: 36px; height: 60px; }

  .news-bar { position: absolute; left: 0; top: 680px; width: 1200px; height: 43px; background: var(--news-bg); border-top: 1px solid #dcdccf; }
  .news-label { position: absolute; left: 97px; top: 11px; font-family: "Roboto", sans-serif; font-size: 16px; color: #555; }
  .news-divider { position: absolute; left: 237px; top: 0; width: 1px; height: 43px; background: var(--rule); }
  .news-item { position: absolute; left: 250px; top: 2px; font-family: "Roboto", sans-serif; font-size: 12.5px; }
  .news-item h2 { font-size: 13px; font-weight: 400; color: var(--accent-red); margin-bottom: 3px; }
  .news-item p { color: #333; }
  .news-controls { position: absolute; left: 1084px; top: 8px; }

  .site-footer { position: absolute; left: 0; top: 723px; width: 1200px; height: 53px; background: var(--footer-bg); }
  .footer-brand {
    position: absolute; left: 52px; top: 19px;
    font-family: "Roboto", sans-serif; font-weight: 500; font-size: 12px; letter-spacing: 0.5px;
    color: var(--tan); text-transform: uppercase; white-space: nowrap;
  }
  .copyright { position: absolute; left: 224px; top: 24px; font-size: 11.5px; color: #6e6e6e; white-space: nowrap; }
  .newsletter { position: absolute; left: 818px; top: 8px; width: 320px; height: 36px; display: flex; }
  .newsletter-field {
    flex: 1; background: var(--field-bg); display: flex; align-items: center; gap: 8px;
    padding-left: 9px; font-size: 12.5px; color: #9a9a9a; border: 1px solid #cfcfc5;
  }
  .newsletter-submit { width: 41px; background: var(--submit-bg); display: flex; align-items: center; justify-content: center; }
</style>
</head>
<body>
  <header class="site-header">
    <div class="brand">Dorvel Buildworks</div>
    <nav class="utility-nav">
      <a href="#">Videos</a><a href="#">News</a><a href="#">Contact</a><a href="#">Terms and Condition</a>
    </nav>
    <nav class="main-nav">
      <a href="#">Home</a><a href="#" class="is-current">About</a><a href="#">Project Photes</a><a href="#">Services</a><a href="#">Dorvel Rewards</a>
    </nav>
  </header>

  <section class="hero">
    <div class="hero-copy">
      <h1>It's Truly a 'Home Sweet Home'!</h1>
      <p>Dorvel Custom Homes is a custom home builder and remodeler based in Portland, Oregon- serving the greater Portland Metro area and Central Oregon.&nbsp; Whether you need a new kitchen or bathroom, a new addition, or you're ready to build your custom dream home, we make the process simple and stress-free.</p>
      <p>With a focus on quality, integrity, sustainability and exceptional project management, our goal is to work with you every step of the way to bring your dreams to reality.&nbsp; From preliminary design ideas to final clean-up, we take care of all the details.&nbsp; All you have to do is enjoy watching your project come to life!</p>
      <p>Please take few minutes to explore our website and get to know us a little better.&nbsp; When you are ready to discuss your project with a Dorvel representative, click here for contact information.&nbsp; We look forward to making your dreams a reality!</p>
      <a href="#" class="read-more">Read More</a>
    </div>
  </section>
  <div class="hero-photo" role="img" aria-label="Interior photo of a finished custom home: warm hardwood floors, grey walls, a staircase landing with a wood and metal railing, and tall windows"></div>
  <svg class="slide-next" viewBox="0 0 36 60" aria-label="Next slide">
    <path d="M0 0 A30 30 0 0 1 0 60 Z" fill="var(--arrow-red)"/>
    <path d="M9 20 L19 30 L9 40" fill="none" stroke="#fff" stroke-width="3.5"/>
  </svg>

  <section class="news-bar">
    <div class="news-label">News &amp; Events</div>
    <div class="news-divider"></div>
    <div class="news-item">
      <h2>House Prices on Up trend</h2>
      <p>Please take few minutes to explore our website and get to know us a</p>
    </div>
    <svg class="news-controls" width="14" height="26" viewBox="0 0 14 26" aria-label="Scroll news">
      <path d="M1 8 L7 2 L13 8 Z" fill="#b5b5b5"/>
      <path d="M1 18 L7 24 L13 18 Z" fill="#b5b5b5"/>
    </svg>
  </section>

  <footer class="site-footer">
    <div class="footer-brand">Dorvel Buildworks</div>
    <div class="copyright">Copyright © 2007-2013 Dorvel Projects. All Rights Reserved.</div>
    <form class="newsletter">
      <div class="newsletter-field">
        <svg width="28" height="18" viewBox="0 0 28 18"><rect x="0.5" y="0.5" width="27" height="17" fill="#c9c9c2" stroke="#b0b0a8"/><path d="M1 1 L14 10 L27 1" fill="none" stroke="#eee" stroke-width="1.5"/></svg>
        <span>Enter email address for Newsletter</span>
      </div>
      <div class="newsletter-submit">
        <svg width="18" height="10" viewBox="0 0 18 10"><path d="M0 5 H16 M12 1 L16 5 L12 9" fill="none" stroke="#fff" stroke-width="1.5"/></svg>
      </div>
    </form>
  </footer>
</body>
</html>
```